Post Sale Flyer For real estate sales in Switzerland

HomeVendra is a real estate agent from Switzerland. Thanks to an innovative mix of digitization and personal contact, HomeVendra brings sellers and qualified buyers together. You will be accompanied from the free evaluation, the first personal consultation, through professional marketing to the handing over of the keys. Payment only upon successful sale of the property. More information is available on our website: https://www.homevendra-example.ch/
Goal:
We would like to set up a post-sale flyer that we can distribute to property owners in the region after the sale of a property in the canton of Aargau (Switzerland).
The aim of this should be to arouse the interest of other property owners in the region in selling their property through HomeVendra.
The message of the flyer should be: We still have interested parties from the previous sale of the property and can sell more property.
Example: We are selling a property at Lindenweg 7 in Aarau. During the sales process, through our marketing activities, we generate various prospective buyers who are interested in this property. However, we can only sell the property to one buyer. The other interested parties get nothing in a first step. Now we want to use the flyer to make real estate owners in the Aarau region aware that we are already in contact with potential buyers of a property in Aarau and that a sale could be interesting.
The call to action should be for property owners to contact our sales team / Head of Sales Lukas Brandt (telephone number 044 812 37 56): https://www.homevendra-example.ch/homevendra/
It would be an advantage to include our Rateflux rating (4.7) for customer satisfaction on the flyer as well as our advantages/USPs.
Basically, the design of the flyer is relatively free as long as it fits our corporate identity and our website https://www.homevendra-example.ch/ and serves the purpose of the flyer. Images can also be chosen freely, although something with real estate and possibly the canton of Aargau (to convey regionality) would certainly be an advantage.
Text can also be freely chosen as long as it serves the purpose of the flyer. For example, it could be as follows:
In the last 12 months we were able to sell x* properties in the canton of Aargau in a short time and had contact with x prospective buyers. Thanks to regional expertise, we broker your property to buyers whose creditworthiness has already been checked, at the best price. Get in contact with us now.
*We would provide the exact figures for finalization as soon as the flyer was accepted internally.
The final flyer design should look modern and appealing, so property owners will contact us.
Target Market(s)
Switzerland
Industry/Entity Type
Immobilien
Requirements
Must have
- Please text in German

```html
<!DOCTYPE html>
<html lang="de">
<head>
<meta charset="utf-8">
<title>HomeVendra – Soeben verkauft</title>
<link rel="stylesheet" href="https://fonts.googleapis.com/css2?family=Great+Vibes&family=Montserrat:wght@300;400;500;600;700;800&display=swap">
<style>
  :root {
    --brand-blue: #1a6dbd;
    --brand-green: #8bc653;
    --ink-dark: #2b2d33;
    --ink-text: #2a2a2e;
    --paper: #ffffff;
    --stage: #dcdcdc;
    --rating-orange: #f0602a;
    --rating-grey: #5a6a8a;
  }
  * { box-sizing: border-box; margin: 0; padding: 0; }
  html, body {
    width: 667px; height: 1200px; overflow: hidden;
    background: var(--stage);
    font-family: "Montserrat", Arial, sans-serif;
  }
  .flyer {
    position: absolute; left: 0; top: 129px;
    width: 667px; height: 942px;
    background: var(--paper);
    overflow: hidden;
    box-shadow: 0 6px 18px rgba(0,0,0,.25);
  }
  .layer { position: absolute; left: 0; top: 0; }

  .brand {
    position: absolute; left: 31px; top: 34px;
    display: flex; align-items: center; gap: 10px;
  }
  .brand-mark { width: 26px; height: 26px; background: var(--brand-blue); }
  .brand-name {
    font-weight: 600; font-size: 40px; color: var(--ink-text);
    letter-spacing: -0.5px; line-height: 1;
  }

  .headline { position: absolute; left: 31px; top: 176px; color: #fff; }
  .headline-script { font-family: "Great Vibes", cursive; font-size: 50px; line-height: 1; font-weight: 400; }
  .headline-main { font-weight: 800; font-size: 43px; line-height: 1; margin-top: 2px; letter-spacing: 0.5px; }
  .headline-sub { font-weight: 300; font-size: 34px; line-height: 1.15; }
  .headline-place { font-weight: 500; font-size: 31px; line-height: 1.15; display: flex; align-items: center; gap: 10px; }
  .headline-place::after { content: ""; width: 104px; height: 2px; background: #fff; }

  .features {
    position: absolute; left: 31px; top: 360px;
    display: grid; grid-template-columns: 180px 180px; row-gap: 6px;
    list-style: none;
    color: #fff; font-size: 13.5px; font-weight: 500;
  }
  .feature { display: flex; align-items: center; gap: 6px; }
  .feature svg { width: 10px; height: 10px; flex: none; }

  .sold-price { position: absolute; left: 380px; top: 404px; width: 287px; text-align: center; color: #fff; }
  .sold-label { font-size: 20px; font-weight: 500; letter-spacing: 2px; line-height: 1.1; }
  .sold-amount { font-size: 34px; font-weight: 800; line-height: 1.3; white-space: nowrap; }

  .thumb {
    position: absolute; top: 443px; width: 147px; height: 147px;
    border: 5px solid var(--brand-green); border-radius: 18px;
  }
  .thumb-bedroom { left: 32px; background: linear-gradient(160deg, #cfc3b2, #8b7660 55%, #5e4d3f); }
  .thumb-living { left: 189px; background: linear-gradient(170deg, #eeeae4, #b9aa98 55%, #6e6055); }

  .rating { position: absolute; left: 372px; top: 513px; display: flex; align-items: center; gap: 12px; }
  .rating-dot { width: 58px; height: 58px; border-radius: 50%; background: var(--brand-blue); flex: none; }
  .rating-score { color: var(--rating-orange); font-size: 22px; font-weight: 400; line-height: 1.2; letter-spacing: 1px; }
  .rating-label { color: var(--rating-grey); font-size: 18px; font-weight: 400; line-height: 1.25; white-space: nowrap; }

  .intro {
    position: absolute; left: 35px; top: 600px; width: 600px;
    font-size: 13px; line-height: 16px; font-weight: 500; color: var(--ink-text);
  }

  .pitch {
    position: absolute; left: 32px; top: 702px; width: 388px;
    font-size: 12.6px; line-height: 15.5px; font-weight: 500; color: #fff;
  }
  .pitch-cta { color: var(--brand-green); font-weight: 700; }

  .contact-title {
    position: absolute; left: 31px; top: 836px;
    color: #fff; font-size: 16px; font-weight: 700; letter-spacing: 0.5px;
  }

  .portrait {
    position: absolute; left: 431px; top: 669px; width: 204px; height: 204px;
    border-radius: 50%; border: 7px solid var(--brand-green);
    background: linear-gradient(180deg, #f2f2f2 0%, #d9d2cb 55%, #3a3a3f 100%);
  }

  .contacts {
    position: absolute; left: 31px; top: 890px; height: 28px;
    display: flex; align-items: center; color: #fff;
  }
  .contact { display: flex; align-items: center; gap: 6px; white-space: nowrap; }
  .contact svg { width: 15px; height: 15px; flex: none; }
  .contact-phone { font-size: 20px; font-weight: 700; letter-spacing: 0.5px; }
  .contact-web, .contact-mail { font-size: 11.3px; font-weight: 500; }
  .divider { width: 2px; height: 22px; background: #fff; margin: 0 12px; }
</style>
</head>
<body>
<main class="flyer">
  <svg class="layer" width="667" height="942" viewBox="0 0 667 942" aria-hidden="true">
    <polygon points="0,90 238,145 400,396 364,463 0,463" fill="var(--brand-blue)"/>
    <polygon points="406,399 667,399 667,487 364,487" fill="var(--brand-green)"/>
    <rect x="0" y="688" width="667" height="170" fill="var(--ink-dark)"/>
    <rect x="0" y="856" width="667" height="86" fill="var(--brand-blue)"/>
    <polygon points="0,827 304,827 288,866 0,866" fill="var(--brand-green)"/>
  </svg>

  <svg class="layer" width="667" height="400" viewBox="0 0 667 400" role="img" aria-label="Foto des verkauften modernen Holzhauses mit Rasen unter blauem Himmel">
    <defs>
      <linearGradient id="house-photo" x1="0" y1="0" x2="0" y2="1">
        <stop offset="0" stop-color="#6d9fd4"/>
        <stop offset="0.35" stop-color="#b9cde0"/>
        <stop offset="0.55" stop-color="#9b7a58"/>
        <stop offset="0.8" stop-color="#4b4a46"/>
        <stop offset="1" stop-color="#6fa43c"/>
      </linearGradient>
    </defs>
    <polygon points="347,0 667,0 667,399 406,399 250,142" fill="url(#house-photo)"/>
  </svg>

  <div class="brand">
    <span class="brand-mark"></span>
    <span class="brand-name">HomeVendra</span>
  </div>

  <h1 class="headline">
    <div class="headline-script">Soeben</div>
    <div class="headline-main">VERKAUFT</div>
    <div class="headline-sub">diese Immobilie</div>
    <div class="headline-place">in Aarau</div>
  </h1>

  <ul class="features">
    <li class="feature"><svg viewBox="0 0 10 10"><circle cx="5" cy="5" r="4.2" fill="none" stroke="#fff" stroke-width="1"/><path d="M3 5.2l1.5 1.4L7.2 3.6" fill="none" stroke="#fff" stroke-width="1"/></svg>3 Schlafzimmer</li>
    <li class="feature"><svg viewBox="0 0 10 10"><circle cx="5" cy="5" r="4.2" fill="none" stroke="#fff" stroke-width="1"/><path d="M3 5.2l1.5 1.4L7.2 3.6" fill="none" stroke="#fff" stroke-width="1"/></svg>Offene Küche</li>
    <li class="feature"><svg viewBox="0 0 10 10"><circle cx="5" cy="5" r="4.2" fill="none" stroke="#fff" stroke-width="1"/><path d="M3 5.2l1.5 1.4L7.2 3.6" fill="none" stroke="#fff" stroke-width="1"/></svg>Waschküche</li>
    <li class="feature"><svg viewBox="0 0 10 10"><circle cx="5" cy="5" r="4.2" fill="none" stroke="#fff" stroke-width="1"/><path d="M3 5.2l1.5 1.4L7.2 3.6" fill="none" stroke="#fff" stroke-width="1"/></svg>Gästezimmer</li>
    <li class="feature"><svg viewBox="0 0 10 10"><circle cx="5" cy="5" r="4.2" fill="none" stroke="#fff" stroke-width="1"/><path d="M3 5.2l1.5 1.4L7.2 3.6" fill="none" stroke="#fff" stroke-width="1"/></svg>2 Badezimmer</li>
    <li class="feature"><svg viewBox="0 0 10 10"><circle cx="5" cy="5" r="4.2" fill="none" stroke="#fff" stroke-width="1"/><path d="M3 5.2l1.5 1.4L7.2 3.6" fill="none" stroke="#fff" stroke-width="1"/></svg>Esszimmer</li>
  </ul>

  <div class="sold-price">
    <div class="sold-label">VERKAUFSPREIS</div>
    <div class="sold-amount">CHF 1'200'200</div>
  </div>

  <div class="thumb thumb-bedroom" role="img" aria-label="Innenfoto des Schlafzimmers"></div>
  <div class="thumb thumb-living" role="img" aria-label="Innenfoto des Wohnzimmers"></div>

  <div class="rating">
    <span class="rating-dot"></span>
    <div>
      <div class="rating-score">4.7★★★★★</div>
      <div class="rating-label">Rateflux Bewertungen</div>
    </div>
  </div>

  <p class="intro">Wir verkaufen eine Immobilie am Lindenweg 7 in Aarau. Während des Verkaufsprozesses gewinnen wir durch unsere Marketingaktivitäten zahlreiche Kaufinteressenten für diese Immobilie. Verkaufen können wir sie jedoch nur an einen Käufer. Die übrigen Interessenten gehen vorerst leer aus.</p>

  <p class="pitch">In den letzten 12 Monaten konnten wir x* Immobilien im Kanton Aargau in kurzer Zeit verkaufen und hatten Kontakt mit x Kaufinteressenten. Dank regionaler Expertise vermitteln wir Ihre Immobilie zum besten Preis an Käufer mit bereits geprüfter Bonität. <span class="pitch-cta">Kontaktieren Sie uns jetzt.</span></p>

  <div class="portrait" role="img" aria-label="Porträtfoto des Verkaufsleiters"></div>

  <h2 class="contact-title">KONTAKTINFORMATIONEN</h2>

  <div class="contacts">
    <span class="contact contact-phone">
      <svg viewBox="0 0 16 16"><path d="M4 1.5l2.2 3-1.3 1.6c.8 1.8 2.2 3.2 4 4l1.6-1.3 3 2.2-1 2.5c-5.8-.4-10.3-4.9-10.7-10.7z" fill="none" stroke="#fff" stroke-width="1.2" stroke-linejoin="round"/></svg>
      044 812 37 56
    </span>
    <span class="divider"></span>
    <span class="contact contact-web">
      <svg viewBox="0 0 16 16"><circle cx="8" cy="8" r="6.5" fill="none" stroke="#fff" stroke-width="1"/><ellipse cx="8" cy="8" rx="3" ry="6.5" fill="none" stroke="#fff" stroke-width="1"/><path d="M1.5 8h13M2.5 4.8h11M2.5 11.2h11" stroke="#fff" stroke-width="1"/></svg>
      www.homevendra-example.ch
    </span>
    <span class="divider"></span>
    <span class="contact contact-mail">
      <svg viewBox="0 0 16 16"><rect x="1.5" y="3.5" width="13" height="9" fill="none" stroke="#fff" stroke-width="1"/><path d="M1.5 3.5L8 9l6.5-5.5" fill="none" stroke="#fff" stroke-width="1"/></svg>
      office@homevendra-example.ch
    </span>
  </div>
</main>
</body>
</html>
```